Business cards design on a high standard

We advise clients on insurance and financial matters, since these clients pay for our advice, the design should have a high standard. Our logo should be included. From the colors we are open for everything.

Colors

Designer to choose colors to be used in the design.

```html
<!DOCTYPE html>
<html lang="en">
<head>
<meta charset="utf-8">
<title>Alpine Counsel – Business Cards</title>
<link href="https://fonts.googleapis.com/css2?family=Open+Sans:wght@400;600;700&display=swap" rel="stylesheet">
<style>
  :root {
    --bg-top: #9a9a9a;
    --bg-bottom: #dcdcdc;
    --card: #2a2a2a;
    --card-edge: #1e1e1e;
    --brand-red: #e0202a;
    --text-light: #ececec;
    --text-muted: #cfcfcf;
    --front-mark: #4a4a4a;
    --divider: #6a6a6a;
  }
  * { margin: 0; padding: 0; box-sizing: border-box; }
  html, body { width: 1200px; height: 900px; overflow: hidden; }
  body {
    background: linear-gradient(180deg, var(--bg-top) 0%, var(--bg-bottom) 100%);
    font-family: "Open Sans", Arial, sans-serif;
    position: relative;
  }
  .card {
    position: absolute;
    left: 320px;
    width: 560px;
    height: 320px;
    background: var(--card);
    border: 1px solid var(--card-edge);
    box-shadow: 0 6px 14px rgba(0,0,0,0.35);
  }
  .card-front { top: 100px; }
  .card-back { top: 470px; }

  .card-front .brand-name {
    position: absolute;
    left: 0; right: 0; top: 50%;
    transform: translateY(-50%);
    text-align: center;
    font-weight: 700;
    font-size: 46px;
    letter-spacing: 2px;
    color: var(--front-mark);
    text-transform: uppercase;
  }

  .card-back .brand-name {
    position: absolute;
    left: 34px; top: 122px;
    width: 220px;
    font-weight: 700;
    font-size: 30px;
    line-height: 1.05;
    letter-spacing: 1px;
    color: var(--brand-red);
    text-transform: uppercase;
  }
  .divider {
    position: absolute;
    left: 270px; top: 66px;
    width: 1px; height: 128px;
    background: var(--divider);
  }
  .contact {
    position: absolute;
    left: 294px; top: 62px;
  }
  .person-name {
    color: var(--brand-red);
    font-weight: 600;
    font-size: 19px;
    line-height: 1.2;
  }
  .person-title {
    color: var(--text-light);
    font-size: 13px;
    margin-bottom: 10px;
  }
  .contact-list { list-style: none; }
  .contact-list li {
    display: flex;
    align-items: center;
    gap: 8px;
    color: var(--text-light);
    font-size: 13px;
    line-height: 22px;
  }
  .contact-list svg { width: 11px; height: 11px; flex: none; }
  .address {
    position: absolute;
    left: 0; right: 0; bottom: 30px;
    text-align: center;
    color: var(--text-light);
    font-size: 13px;
    letter-spacing: 0.2px;
  }
</style>
</head>
<body>
  <section class="card card-front">
    <div class="brand-name">Alpine Counsel</div>
  </section>

  <section class="card card-back">
    <div class="brand-name">Alpine<br>Counsel</div>
    <div class="divider"></div>
    <div class="contact">
      <div class="person-name">Daniel Hartley</div>
      <div class="person-title">President</div>
      <ul class="contact-list">
        <li>
          <svg viewBox="0 0 12 12" aria-hidden="true"><path d="M2.5 0.8 L4.6 3 L3.6 4.4 Q4.6 6.6 7.6 8.4 L9 7.4 L11.2 9.5 L9.8 11.2 Q5.5 11 2.6 8 Q0.6 5.4 0.8 2.2 Z" fill="var(--brand-red)"/></svg>
          (555) 014-2286
        </li>
        <li>
          <svg viewBox="0 0 12 12" aria-hidden="true"><rect x="0.8" y="2.2" width="10.4" height="7.6" fill="none" stroke="var(--brand-red)" stroke-width="1.3"/><path d="M0.8 2.4 L6 6.6 L11.2 2.4" fill="none" stroke="var(--brand-red)" stroke-width="1.3"/></svg>
          daniel@alpinecounsel.com
        </li>
        <li>
          <svg viewBox="0 0 12 12" aria-hidden="true"><circle cx="6" cy="6" r="5.2" fill="none" stroke="var(--brand-red)" stroke-width="1.2"/><ellipse cx="6" cy="6" rx="2.2" ry="5.2" fill="none" stroke="var(--brand-red)" stroke-width="1"/><path d="M0.8 6 H11.2" stroke="var(--brand-red)" stroke-width="1"/></svg>
          www.alpinecounsel.com
        </li>
      </ul>
    </div>
    <div class="address">48 Harbor Point Drive, Coral Bay, Florida, 33190</div>
  </section>
</body>
</html>
```